依頼詳細
タイ古式マッサージの看板ポスターを作成依頼をお願いします。
サイズはA2サイズです。よろしくお願いします。
例文は添付致します。
記載項目
店舗名、電話番号、ロゴ
希望イメージ
シンプル 複雑
単色 カラフル
暗い 明るい
日常 高級
遊び心 厳粛
未来的 伝統的
女性的 男性的
希望する色
赤系、茶系、緑系、グレー系
納品ファイル
• 高解像度JPG (.jpg)
• イラストレーター形式 (.ai)
補足説明
スタンド看板にしますのでA2サイズでなく原稿サイズ435x940でお願いします。
すみませんがよろしくお願いします。

色がとてもいいです!! パッと見て目立つしわかりやすいと思いました。
ありがとうございました。

この度は、皆様方にご提案頂きまして誠にありがとうございました。
また、何かございましたらよろしくお願いします。
ありがとうございました。

```html
<!DOCTYPE html>
<html lang="ja">
<head>
<meta charset="UTF-8">
<title>タイ古式マッサージ 看板</title>
<link href="https://fonts.googleapis.com/css2?family=Shippori+Mincho+B1:wght@700;800&family=Noto+Serif+JP:wght@700;900&family=Noto+Sans+JP:wght@400;500;700;900&display=swap" rel="stylesheet">
<style>
  :root{
    --gold-light:#e3c987;
    --gold:#cdaa5e;
    --gold-dark:#a9843d;
    --wine:#7b1c24;
    --wine-deep:#5a1118;
    --red:#c22a2c;
    --ink:#1c1410;
    --ink-soft:#3a2c20;
    --white:#fffaf0;
  }
  *{margin:0;padding:0;box-sizing:border-box}
  html,body{width:1200px;height:2592px;overflow:hidden;background:#fff}
  .poster{
    position:relative;width:1200px;height:2592px;overflow:hidden;
    background:radial-gradient(ellipse at 50% 35%,var(--gold-light) 0%,var(--gold) 55%,var(--gold-dark) 100%);
    font-family:"Noto Sans JP",sans-serif;color:var(--ink);
  }
  .frame{position:absolute;inset:30px;border:3px solid var(--white);border-radius:18px;pointer-events:none}
  .corner{position:absolute;width:110px;height:110px;background:linear-gradient(135deg,rgba(255,250,240,.55),rgba(255,250,240,0))}
  .corner.tl{left:30px;top:30px;border-top-left-radius:18px}
  .corner.tr{right:30px;top:30px;transform:scaleX(-1);border-top-left-radius:18px}
  .corner.bl{left:30px;bottom:30px;transform:scaleY(-1);border-top-left-radius:18px}
  .corner.br{right:30px;bottom:30px;transform:scale(-1,-1);border-top-left-radius:18px}

  .title-ring{position:absolute;left:150px;top:90px;width:700px;height:640px}
  .flame{position:absolute;left:810px;top:40px;width:330px;height:720px;border-radius:50% 50% 45% 45%;
    background:radial-gradient(ellipse at 50% 45%,rgba(154,42,48,.75) 0%,rgba(123,28,36,.55) 50%,rgba(123,28,36,0) 72%)}
  .title{position:absolute;left:0;top:0;width:1200px;height:720px}
  .title-tai{position:absolute;left:330px;top:140px;font-family:"Shippori Mincho B1",serif;font-weight:800;
    font-size:230px;line-height:1;color:var(--wine);letter-spacing:-6px}
  .title-koshiki{position:absolute;left:440px;top:420px;width:260px;height:100px;background:var(--wine);
    border-radius:18px;color:var(--white);font-family:"Noto Serif JP",serif;font-weight:900;font-size:76px;
    line-height:100px;text-align:center;letter-spacing:6px}
  .title-massage{position:absolute;left:370px;top:525px;font-family:"Shippori Mincho B1",serif;font-weight:800;
    font-size:122px;line-height:1.1;color:var(--wine);letter-spacing:-2px;white-space:nowrap}

  .lead{position:absolute;left:88px;top:860px;width:1060px;padding-left:34px}
  .lead::before{content:"";position:absolute;left:0;top:6px;width:16px;height:140px;background:var(--wine)}
  .lead h2{font-family:"Noto Serif JP",serif;font-weight:900;font-size:58px;line-height:1.25;color:var(--ink);white-space:nowrap}

  .voices{position:absolute;left:96px;top:1090px;width:1020px;font-weight:700;font-size:33px;line-height:1.5;color:var(--ink-soft);white-space:nowrap;letter-spacing:-.5px}
  .voices .quote{color:var(--red)}
  .body-copy{position:absolute;left:96px;top:1215px;width:1010px;font-size:28px;font-weight:500;line-height:1.6;color:var(--ink-soft);text-align:justify}

  .illustration{position:absolute;left:150px;top:1430px;width:900px;height:630px;
    background:radial-gradient(ellipse at 50% 60%,rgba(110,40,50,.5) 0%,rgba(60,40,40,.3) 45%,rgba(205,170,94,0) 72%)}

  .effect{position:absolute;left:100px;top:2080px;width:1000px;font-weight:900;font-size:40px;color:var(--red);
    padding-bottom:12px;border-bottom:4px dotted var(--wine);white-space:nowrap}

  .prices{position:absolute;left:96px;top:2175px;width:1010px;display:flex;gap:50px;align-items:center}
  .price{display:flex;align-items:center;gap:14px}
  .price .mins{width:86px;height:86px;border-radius:50%;background:var(--wine);color:var(--white);
    font-weight:900;font-size:30px;line-height:86px;text-align:center;flex:none}
  .price .amount{font-weight:900;font-size:108px;line-height:1;color:var(--wine);letter-spacing:-2px;white-space:nowrap}
  .price .yen{font-size:70px}
  .price .tax{display:inline-block;font-size:22px;font-weight:700;vertical-align:top;margin-left:4px;margin-top:6px;letter-spacing:0}

  .footer{position:absolute;left:60px;top:2360px;width:1080px;border-top:3px solid var(--white);padding-top:26px;
    display:flex;justify-content:space-between;align-items:flex-start}
  .brand{display:flex;align-items:center;gap:16px;padding-left:24px}
  .brand-dot{width:26px;height:26px;border-radius:50%;background:var(--white)}
  .brand-text{color:var(--white);font-weight:700;font-size:76px;line-height:1;letter-spacing:4px}
  .brand-text small{display:block;font-size:22px;letter-spacing:3px;margin-top:6px}
  .contact{color:var(--white);padding-right:20px}
  .tel{display:flex;align-items:center;gap:10px;font-weight:700;font-size:66px;line-height:1}
  .tel svg{width:56px;height:56px}
  .hours{font-size:24px;font-weight:500;margin-top:10px;padding-left:62px}
</style>
</head>
<body>
<div class="poster">
  <div class="frame"></div>
  <div class="corner tl" role="img" aria-label="角の装飾模様"></div>
  <div class="corner tr" role="img" aria-label="角の装飾模様"></div>
  <div class="corner bl" role="img" aria-label="角の装飾模様"></div>
  <div class="corner br" role="img" aria-label="角の装飾模様"></div>

  <svg class="title-ring" viewBox="0 0 700 640" aria-hidden="true">
    <path d="M170 600 A290 290 0 0 1 560 60" fill="none" stroke="var(--wine)" stroke-width="14" stroke-linecap="round"/>
  </svg>
  <div class="flame" role="img" aria-label="タイ伝統の炎形唐草装飾"></div>

  <h1 class="title">
    <span class="title-tai">タイ</span>
    <span class="title-koshiki">古式</span>
    <span class="title-massage">マッサージ</span>
  </h1>

  <section class="lead">
    <h2>デスクワークが多く、辛い首こりや<br>肩こり・体の疲れがヒドイあなたに。</h2>
  </section>

  <p class="voices"><span class="quote">「気づいたら、寝ていた」「ビックリするほど、体が軽くなった」</span><br>などの声をいただくタイ古式マッサージを体験してみませんか？</p>

  <p class="body-copy">別名「二人で行うヨガ」と言われ、もむ、押すだけでなくストレッチ施術で血行を促しながら筋肉の柔軟性を高めていきます。何だかプロレス技を掛けられているようなストレッチですが、ゆっくりと体がほぐされていくので痛くなく、「世界で一番気持ちいいマッサージ」と言われています。</p>

  <div class="illustration" role="img" aria-label="施術者が寝そべる女性の両腕を引いてストレッチするタイ古式マッサージのイラスト"></div>

  <p class="effect">クイックマッサージにはない効果を実感できます！</p>

  <div class="prices">
    <div class="price"><span class="mins">30分</span><span class="amount">3,500<span class="yen">円</span><span class="tax">(税込)</span></span></div>
    <div class="price"><span class="mins">60分</span><span class="amount">5,900<span class="yen">円</span><span class="tax">(税込)</span></span></div>
  </div>

  <footer class="footer">
    <div class="brand">
      <span class="brand-dot"></span>
      <span class="brand-text">LUMORA<small>Training studio</small></span>
    </div>
    <div class="contact">
      <div class="tel">
        <svg viewBox="0 0 24 24" aria-hidden="true"><path fill="var(--white)" d="M6.6 10.8a15.1 15.1 0 0 0 6.6 6.6l2.2-2.2c.3-.3.7-.4 1-.2 1.1.4 2.3.6 3.6.6.6 0 1 .4 1 1V20c0 .6-.4 1-1 1A17 17 0 0 1 3 4c0-.6.4-1 1-1h3.5c.6 0 1 .4 1 1 0 1.2.2 2.4.6 3.6.1.3 0 .7-.2 1z"/></svg>
        <span>03-4821-7306</span>
      </div>
      <p class="hours">受付時間 / 10:00～21:00（最終 20:30）</p>
    </div>
  </footer>
</div>
</body>
</html>
```